We need a flyer where we promote a workshop to our members of the jewish community www.qvb-gemeinde.example . The workshop is calles "guidance in ten seasons presented by QVB. We would like to see a flyer with the below text is used and also some pictures (attached). The flyer should come over as cool, fresh, innovative for a younger crowd so called young professionals (age 28-35).
TITLE.
"Guidance in Ten Seasons.
SUBTITLE.
Your systematic self-coaching roadmap to power and impact—and your future.”
TEXT.
Dr. Martin K. Halvorsen is the CEO Emeritus of Alpine Advisory Partners—he made an exit in 2013. He is the award-winning author of 8 books, including "Plan-Into-Motion," "Speak or Falter" and "The Cantor and the Chairman.”
For the past 20 years he has taught leadership at Harwick University in New York and at BKU (Lindenberg University) to prepare future CEOs and other leaders in business, government , nonprofits and the military.
Now, in a process exclusively designed for QVB’s next generation of emerging leaders, Martin unpacks his leadership secrets in 3 action-packed labs—reduced to the max:
Lab 1. Guidance in Ten Seasons: The Summit Guide Triangle®. Self-Assessment. Self-Leadership: “The Lantern.” 5-Year Vision. 100-Day Catalytic Project.
Lab 2. Leading Through Language. Relationship: Building Trust. Plan-Into-Motion. Cockpit.
Lab 3. Debrief and Scale-Up. Sustainability. Action Tools.
Do you want to build your own future and a life you love? Do you want to jump-start that future and life over 100 days while learning a toolbox of leadership skills, networking with like-minded people—and even get some pizza? Then join us.
Target Market(s)
young professionals age 28-35

```html
<!DOCTYPE html>
<html lang="en">
<head>
<meta charset="utf-8">
<title>Guidance in Ten Seasons – Workshop Flyer</title>
<link href="https://fonts.googleapis.com/css2?family=Bebas+Neue&family=Montserrat:ital,wght@0,400;0,600;0,700;1,600&display=swap" rel="stylesheet">
<style>
  :root {
    --flyer-red: #eb4e4d;
    --ink-white: #ffffff;
    --depth-grey: #c9c9c9;
    --band-text: #1f1f1f;
    --pill-yellow: #fdd563;
    --pill-text: #3a2a10;
    --page-bg: #ffffff;
  }
  * { margin: 0; padding: 0; box-sizing: border-box; }
  html, body { width: 1200px; height: 1200px; overflow: hidden; background: var(--page-bg); }
  .flyer {
    position: absolute; left: 176px; top: 0; width: 848px; height: 1200px;
    background: var(--flyer-red); color: var(--ink-white);
    font-family: "Montserrat", Arial, sans-serif;
  }
  .frame { position: absolute; left: 0; top: 0; width: 848px; height: 1200px; }
  .eyebrow {
    position: absolute; left: 0; right: 0; top: 40px; text-align: center; white-space: nowrap;
    font-family: "Bebas Neue", Impact, sans-serif; font-size: 30px; letter-spacing: 5px; line-height: 30px;
  }
  .eyebrow span { background: var(--flyer-red); padding: 0 10px 0 15px; }
  .hero-art {
    position: absolute; left: 204px; top: 92px; width: 446px; height: 164px;
    background: linear-gradient(180deg, rgba(255,255,255,0.10), rgba(255,255,255,0.22));
    border-radius: 6px;
  }
  .headline {
    position: absolute; left: 0; right: 0; text-align: center; white-space: nowrap;
    font-family: "Bebas Neue", Impact, sans-serif; color: var(--ink-white);
    text-shadow: -6px 3px 0 var(--depth-grey);
    line-height: 1;
  }
  .headline--top { top: 266px; font-size: 156px; letter-spacing: 1px; }
  .headline--mid { top: 388px; font-size: 140px; letter-spacing: 8px; }
  .headline--low { top: 512px; font-size: 160px; }
  .rule { position: absolute; top: 449px; height: 2px; background: var(--ink-white); }
  .rule--left { left: 106px; width: 264px; }
  .rule--right { left: 478px; width: 258px; }
  .subtitle {
    position: absolute; left: 0; right: 0; top: 686px; text-align: center;
    font-weight: 700; font-size: 20.5px; line-height: 29px; text-transform: uppercase; letter-spacing: 0.3px;
  }
  .speaker {
    position: absolute; left: 0; right: 0; top: 752px; text-align: center; white-space: nowrap;
    font-family: "Bebas Neue", Impact, sans-serif; font-size: 68px; line-height: 68px;
  }
  .bio {
    position: absolute; left: 47px; top: 827px; width: 754px; height: 122px;
    background: var(--ink-white); color: var(--band-text);
    font-style: italic; font-weight: 600; font-size: 11.6px; line-height: 15.5px;
    text-align: center; padding: 16px 36px 0;
  }
  .bio p + p { margin-top: 7px; }
  .labs { position: absolute; left: 0; right: 0; top: 960px; text-align: center; }
  .lab-tag {
    display: inline-block; background: var(--pill-yellow); color: var(--pill-text);
    font-weight: 600; font-size: 12.5px; line-height: 25px; height: 25px; padding: 0 17px; border-radius: 13px;
  }
  .lab-desc { font-size: 12.5px; line-height: 17px; margin: 3px 0 9px; }
  .site {
    position: absolute; left: 0; right: 0; top: 1146px; text-align: center; white-space: nowrap;
    font-weight: 600; font-size: 17px; letter-spacing: 5px; line-height: 22px; text-transform: uppercase;
  }
  .site span { background: var(--flyer-red); padding: 0 6px 0 11px; }
</style>
</head>
<body>
  <main class="flyer">
    <svg class="frame" viewBox="0 0 848 1200" aria-hidden="true">
      <path d="M45 55 H804 V1157 H45 Z" fill="none" stroke="#ffffff" stroke-width="2.5"/>
    </svg>

    <p class="eyebrow"><span>Guidance in Ten Seasons presented by QVB</span></p>

    <div class="hero-art" role="img" aria-label="Flat illustration of a group of young professionals following arrows toward a leader with a glowing light bulb idea"></div>

    <h1>
      <span class="headline headline--top">Guidance</span>
      <span class="rule rule--left"></span>
      <span class="headline headline--mid">In</span>
      <span class="rule rule--right"></span>
      <span class="headline headline--low">Ten Seasons</span>
    </h1>

    <p class="subtitle">Your systematic self-coaching roadmap to<br>power and impact—and your future</p>

    <p class="speaker">Dr. Martin K. Halvorsen</p>

    <section class="bio">
      <p>Dr. Martin K. Halvorsen is the CEO Emeritus of Alpine Advisory Partners—he made an exit in 2013. He is the award-winning author of 8 books, including "Plan-Into-Motion," "Speak or Falter" and "The Cantor and the Chairman.”</p>
      <p>For the past 20 years he has taught leadership at Harwick University in New York and at BKU (Lindenberg University) to prepare future CEOs and other leaders in business, government , nonprofits and the military.</p>
    </section>

    <section class="labs">
      <span class="lab-tag">LAB 1</span>
      <p class="lab-desc">Guidance in Ten Seasons: The Summit Guide Triangle®. Self-Assessment. Self-Leadership:<br>“The Lantern.” 5-Year Vision. 100-Day Catalytic Project.</p>
      <span class="lab-tag">LAB 2</span>
      <p class="lab-desc">Leading Through Language. Relationship: Building Trust. Plan-Into-Motion. Cockpit.</p>
      <span class="lab-tag">LAB 3</span>
      <p class="lab-desc">Debrief and Scale-Up. Sustainability. Action Tools.</p>
    </section>

    <p class="site"><span>www.qvb-gemeinde.example</span></p>
  </main>
</body>
</html>
```